Brand and Marketing Coach Needs PDF Designed

I have content that i need placed into a simple but great PDF design. The PDF is about the formula I use to build personal brands. This is geared towards entrepreneurs, experts, coaches, therapists, wellness practitioners, and indpendent business owners who serve to improve the lives of others.
The company name is changing from BrovelStudio to Branding with the Crowd (I don't have that logo yet, so working backwards a bit. For now, the BrovelStudio logo can be used.) My brand is NOT formal and corporate, but it's also not neon-pink and screaming at you. It's down to earth, hip, a bit modern but warm. It's about no BS and authenticity. The final deliverable should make the reader feel focused, smart, motivated and hopeful.

Target Market(s)

Conscious entrepreneurs and small business owners. this one is specifically for pharmacy entrepreneurs but this will be used for various audiences later.

Font styles to use
Sans Serif

Colors
eaf1f7
3377b5
6b449b
f37122
faa54b
f68e4e
ffc214

Requirements
Must have
• Modern design. colors that match logo - 4e5583 (i think that is the blue.) d65a40.
• Could have these colors as well: c6a254, 01bcc3
• But open to other colors
Nice to have
• I'd like to see some ways to make this PDF simple and readable, and eye-catching. I'd also like to use the uploaded ebooks for design ideas.
Should not have
• neon colors, clip art

```html
<!DOCTYPE html>
<html lang="en">
<head>
<meta charset="utf-8">
<title>Solo Signal Method – What This Is</title>
<link rel="stylesheet" href="https://fonts.googleapis.com/css2?family=Arimo&family=Rajdhani:wght@300;400;500;600&display=swap">
<style>
  :root {
    --page-bg: #ffffff;
    --brand-purple: #6b449b;
    --brand-navy: #4e5583;
    --body-grey: #707070;
    --ink: #1a1a1a;
    --on-purple: #f1ecf7;
  }
  html, body {
    margin: 0;
    padding: 0;
    overflow: hidden;
    background: var(--page-bg);
  }
  .page {
    position: relative;
    width: 1200px;
    height: 927px;
    overflow: hidden;
    background: var(--page-bg);
    font-family: "Rajdhani", sans-serif;
  }
  .intro {
    position: absolute;
    left: 295px;
    top: 191px;
    margin: 0;
    font-family: "Arimo", sans-serif;
    font-size: 17.9px;
    color: var(--ink);
  }
  .section-title {
    position: absolute;
    left: 291px;
    top: 220px;
    margin: 0;
    font-weight: 500;
    font-size: 35px;
    letter-spacing: 0.6px;
    color: var(--brand-purple);
  }
  .copy {
    position: absolute;
    left: 296px;
    width: 775px;
    margin: 0;
    font-weight: 400;
    font-size: 17.7px;
    letter-spacing: 0.1px;
    line-height: 22px;
    color: var(--body-grey);
  }
  .copy--lead { top: 273px; line-height: 31px; }
  .copy--emphasis { top: 347px; color: var(--ink); font-weight: 500; }
  .copy--blocks { top: 410px; }
  .copy--background { top: 472px; }
  .copy--closing { top: 598px; }
  .callout {
    position: absolute;
    left: 282px;
    top: 504px;
    width: 795px;
    height: 84px;
    box-sizing: border-box;
    padding: 10px 14px 0 14px;
    background: var(--brand-purple);
    color: var(--on-purple);
    font-weight: 300;
    font-size: 20px;
    line-height: 21px;
    text-align: justify;
    margin: 0;
  }
  .footer-rule {
    position: absolute;
    left: 297px;
    top: 846px;
    width: 903px;
    height: 4px;
    background: var(--brand-purple);
  }
  .brand-name {
    position: absolute;
    left: 56px;
    top: 826px;
    margin: 0;
    font-weight: 600;
    font-size: 32px;
    line-height: 36px;
    color: var(--brand-navy);
  }
</style>
</head>
<body>
<main class="page">
  <p class="intro">I'm so glad you're here! Before we start, a few things:</p>
  <h1 class="section-title">WHAT THIS IS</h1>

  <p class="copy copy--lead">&nbsp;The Solo Signal Method consists of the exact steps I take to create unique and authentic brands for my clients. It is also what will drive your entire marketing strategy.</p>

  <p class="copy copy--emphasis">One mistake I see entrepreneurs make is to consider BRAND as a separate entity from MARKETING. These two essential elements of your business are deeply connected.</p>

  <p class="copy copy--blocks">Rather than giving you the elements of a brand, which is really the end product of this work – what I'm giving you here are the essential building blocks, designed to help you discover and unleash your unique brand.</p>

  <p class="copy copy--background">This is what most people don't tell you about because it's the deep work that happens in the background.</p>

  <p class="callout">When you go through the steps to create your own brand, not only do you build a brand that attracts your ideal clients, but your marketing falls into place, and you finally learn what makes you stand way above the competition.</p>

  <p class="copy copy--closing">Yes, it's true. When you take the time to create your brand, your messaging and marketing strategy fall into place. And this formula is what gets you there.</p>

  <p class="brand-name">BrovelStudio</p>
  <div class="footer-rule"></div>
</main>
</body>
</html>
```